Innovation and Optimisation Consultancy business needs a Wix website design

The task details are in the attached project brief. The attached pdf should give you a good outline of what is required. Colour guidance and look and feel guidelines are in the pdf file. The company is based in S.E.Asia.

Can be done as design files, but prefer it to be designed direct in WIX.

If you have any questions just ask.

I really don't know what will attract clients to my website so am leaving it to you to do something inspiring and innovative.

Target Market(s)

Organisations that don't just want to compete in their market, but that want to be number one in their market and be sure they stay there.

Industry/Entity Type

All

Requirements
Must have
• I don't know, I specialise in optimising businesses and inventing new products.
Nice to have
• Surprise me.

```html
<!DOCTYPE html>
<html lang="en">
<head>
<meta charset="utf-8">
<title>Brightpath – Innovative Solution Consulting Service</title>
<link href="https://fonts.googleapis.com/css2?family=Poppins:ital,wght@0,300;0,400;0,500;0,600;0,700;1,400&display=swap" rel="stylesheet">
<style>
:root{
  --navy:#0b1f4f;
  --navy-deep:#061640;
  --hero-a:#3f5f95;
  --hero-b:#6f8fbf;
  --maroon:#4a1228;
  --crimson:#8c0f2e;
  --green:#4cc46f;
  --green-line:#b9d79a;
  --gold-line:#d8cfa0;
  --divider:#b8c0cc;
  --ink:#1c1c24;
  --muted:#555a66;
  --slate:#7a8aa2;
  --footer:#6b7c98;
  --footer-dark:#4c5b78;
  --cream:#f7e6d3;
  --white:#ffffff;
  --star:#f3b51d;
}
*{box-sizing:border-box;margin:0;padding:0}
html,body{width:1200px;height:4383px;overflow:hidden}
body{font-family:"Poppins",sans-serif;color:var(--ink);background:var(--white);position:relative}
.abs{position:absolute}

/* hero */
.hero{position:absolute;left:0;top:0;width:1200px;height:713px;background:linear-gradient(100deg,var(--hero-a) 0%,#5877ad 45%,var(--hero-b) 100%);overflow:hidden}
.hero-photo{position:absolute;right:0;top:0;width:620px;height:713px;background:radial-gradient(ellipse at 60% 40%,#c9d6ea 0%,#8fb0d6 35%,rgba(90,130,190,0) 75%)}
.logo{position:absolute;left:121px;top:22px;font-size:30px;color:var(--white);font-weight:400;letter-spacing:.3px}
.nav a{position:absolute;top:30px;color:var(--white);font-size:16px;text-decoration:none;white-space:nowrap}
.nav a.active::after{content:"";position:absolute;left:0;right:0;bottom:-7px;height:2px;background:#7fe0e9}
.btn-green{position:absolute;left:953px;top:24px;width:141px;height:41px;border-radius:21px;background:var(--green);color:var(--white);font-size:14px;display:flex;align-items:center;justify-content:center;font-weight:500}
.welcome{position:absolute;left:114px;top:219px;color:var(--white);font-size:19px;display:flex;align-items:center;gap:12px}
.welcome .rule{display:block;width:80px;height:1px;background:var(--white)}
.hero h1{position:absolute;left:114px;top:246px;color:var(--white);font-size:51px;line-height:57px;font-weight:700;white-space:nowrap}
.hero h1 .light{font-weight:400}
.hero p{position:absolute;left:114px;top:380px;width:380px;color:var(--white);font-size:14.5px;line-height:22px}
.btn-navy{position:absolute;left:114px;top:441px;width:169px;height:47px;border-radius:24px;background:var(--navy-deep);color:var(--white);font-size:15px;display:flex;align-items:center;justify-content:center;font-weight:500}
.divider{position:absolute;left:0;width:1200px;height:3px;background:var(--divider)}

/* section titles */
.title{position:absolute;left:0;width:1200px;text-align:center;font-size:44px;font-weight:600;color:var(--ink)}
.title .light{font-weight:400}
.title-rule{position:absolute;left:577px;width:46px;height:3px;background:#3b4a6b}

/* photo rings */
.ring{position:absolute;border-radius:50%;border:3px solid #d4d7dd;background:var(--white);box-shadow:0 10px 40px rgba(0,0,0,.08)}
.ring .fill{position:absolute;inset:12px;border-radius:50%}
.link{position:absolute;height:4px}
.link.gold{background:var(--gold-line)}
.link.green{background:var(--green-line)}
.link.v{width:4px;height:auto}

/* cards */
.card{position:absolute;width:390px;height:109px;background:var(--white);border-radius:55px;box-shadow:0 6px 22px rgba(0,0,0,.09)}
.card h3{position:absolute;font-size:17.5px;font-weight:500;color:var(--ink);white-space:nowrap}
.card p{position:absolute;font-size:11px;line-height:17px;color:var(--muted);width:240px}
.icon-dot{position:absolute;width:84px;height:84px;border-radius:50%;display:flex;align-items:center;justify-content:center}
.icon-dot.maroon{background:var(--maroon);box-shadow:0 0 0 6px #efe6ea}
.icon-dot.green{background:var(--green);box-shadow:0 0 0 6px #e3f5e8}

/* benefits */
.benefits-bg{position:absolute;left:0;top:2043px;width:1200px;height:881px;background:linear-gradient(180deg,var(--cream) 0%,#fbefe3 55%,#f8e2cf 100%)}
.diamond{position:absolute;width:246px;height:246px;background:var(--white);transform:rotate(45deg);box-shadow:0 6px 24px rgba(0,0,0,.06)}
.diamond.hot{background:var(--crimson)}
.d-copy{position:absolute;width:220px;text-align:center}
.d-copy h4{font-size:19px;font-weight:600;color:#163a77;margin:8px 0 10px}
.d-copy p{font-size:12px;line-height:18px;color:var(--muted)}
.d-copy.hot h4,.d-copy.hot p{color:var(--white)}

/* quote */
.quote{position:absolute;left:114px;top:2779px;width:970px;height:213px;background:var(--slate);border:2px solid #9aa7ba;box-shadow:inset 0 0 0 8px #8291a7}
.quote .mark{position:absolute;left:82px;top:40px;font-size:120px;line-height:120px;color:var(--white);font-weight:700}
.quote blockquote{position:absolute;left:175px;top:50px;width:740px;font-size:24px;line-height:34px;color:var(--white);font-style:italic}
.quote cite{position:absolute;left:166px;top:132px;font-size:19px;color:var(--white);font-style:normal;font-weight:500}

/* testimonials */
.t-card{position:absolute;top:3188px;width:286px;height:279px;background:var(--white);border:1px solid #dfe3ea;border-radius:6px;box-shadow:0 4px 16px rgba(0,0,0,.05)}
.t-card .q{position:absolute;left:42px;top:22px;font-size:28px;color:#4c6b5e;font-family:Georgia,serif}
.t-card p{position:absolute;left:44px;top:66px;width:210px;font-size:10.5px;line-height:18px;color:#333}
.t-card .who{position:absolute;left:44px;top:228px;display:flex;align-items:center;gap:12px}
.avatar{width:30px;height:30px;border-radius:50%;background:#a8b3c4}
.stars{color:var(--star);font-size:11px;letter-spacing:1px;line-height:12px}
.who b{font-size:11px;font-weight:600;display:block}
.arrow{position:absolute;top:3315px;font-size:30px;color:var(--navy);font-weight:300}

/* contact */
.footer-bg{position:absolute;left:0;top:3833px;width:1200px;height:478px;background:var(--footer)}
.footer-bar{position:absolute;left:0;top:4311px;width:1200px;height:72px;background:var(--footer-dark);color:var(--white);font-size:11px;text-align:center;line-height:72px}
.contact{position:absolute;left:155px;top:3530px;width:892px;height:456px;background:radial-gradient(ellipse at 30% 90%,#1c4a94 0%,var(--navy) 45%,#071845 100%)}
.contact h2{position:absolute;left:0;top:57px;width:892px;text-align:center;color:var(--white);font-size:34px;font-weight:400}
.contact h2 b{font-weight:700}
.field{position:absolute;background:var(--white);font-size:12px;color:#333;display:flex;align-items:center;gap:8px;padding-left:16px}
.field i{display:inline-block;width:12px;height:12px;border-radius:50%;background:#9aa2ad}
.submit{position:absolute;left:378px;top:359px;width:151px;height:38px;border-radius:19px;background:#5d6f8e;color:var(--white);font-size:14px;display:flex;align-items:center;justify-content:center}

/* footer */
.f-logo{position:absolute;left:158px;top:4045px;font-size:30px;color:var(--white)}
.f-about{position:absolute;left:158px;top:4098px;width:210px;font-size:11px;line-height:16px;color:var(--white)}
.f-head{position:absolute;top:4052px;font-size:17px;font-weight:600;color:var(--white);letter-spacing:.5px;padding-left:14px;border-left:2px solid var(--white);line-height:18px}
.f-list{position:absolute;top:4132px;list-style:none;color:var(--white);font-size:15px;line-height:30px}
.f-item{position:absolute;left:640px;display:flex;gap:14px;color:var(--white);font-size:13.5px;line-height:19px;align-items:center}
.f-item .dot{width:32px;height:32px;border-radius:50%;background:var(--white);display:flex;align-items:center;justify-content:center}
.social{position:absolute;top:4100px;width:26px;height:26px;border-radius:50%;border:2px solid var(--white)}
</style>
</head>
<body>

<section class="hero">
  <div class="hero-photo" role="img" aria-label="Portrait of a woman with a glowing digital technology overlay"></div>
  <div class="logo">Brightpath</div>
  <nav class="nav">
    <a class="active" style="left:574px">Home</a>
    <a style="left:684px">About Us</a>
    <a style="left:820px">Services</a>
  </nav>
  <div class="btn-green">Contact Us ›</div>
  <div class="welcome">Welcome to Brightpath <span class="rule"></span></div>
  <h1>Innovative Solution<br><span class="light">Consulting Service</span></h1>
  <p>Lorem ipsum dolor sit amet consectetur adipiscing elit sed do eiusmod tempor incididunt ut</p>
  <div class="btn-navy">Contact Us ›</div>
  <svg class="abs" style="left:113px;top:549px" width="100" height="100" viewBox="0 0 100 100">
    <defs><path id="scroll-path" d="M50 50 m-40 0 a40 40 0 1 1 80 0 a40 40 0 1 1 -80 0"/></defs>
    <text fill="#fff" font-size="10" font-family="Poppins,sans-serif" letter-spacing="2.6"><textPath href="#scroll-path">SCROLL DOWN · SCROLL DOWN ·</textPath></text>
    <circle cx="50" cy="50" r="24" fill="none" stroke="#fff" stroke-width="1.5"/>
    <path d="M50 40 V60 M43 53 L50 60 L57 53" fill="none" stroke="#fff" stroke-width="1.5"/>
  </svg>
</section>
<div class="divider" style="top:712px"></div>

<!-- Problems -->
<h2 class="title" style="top:782px">Problems</h2>
<div class="title-rule" style="top:841px"></div>
<div class="ring" style="left:91px;top:860px;width:452px;height:452px">
  <div class="fill" role="img" aria-label="Stressed man holding his head in front of a laptop" style="background:linear-gradient(160deg,#e7e2d6,#c9c28c 55%,#9a8f7a)"></div>
</div>
<div class="link gold" style="left:543px;top:1082px;width:70px"></div>
<div class="link gold v" style="left:611px;top:932px;height:304px"></div>
<div class="link gold" style="left:611px;top:932px;width:72px"></div>
<div class="link gold" style="left:611px;top:1082px;width:72px"></div>
<div class="link gold" style="left:611px;top:1232px;width:72px"></div>

<div class="card" style="left:677px;top:878px">
  <div class="icon-dot maroon" style="left:16px;top:12px"><svg width="40" height="40" viewBox="0 0 40 40" fill="none" stroke="#fff" stroke-width="1.6"><circle cx="20" cy="20" r="7"/><circle cx="20" cy="20" r="14" stroke-dasharray="4 3"/></svg></div>
  <h3 style="left:118px;top:22px">Problem Heading</h3>
  <p style="left:118px;top:48px">orem ipsum dolor sit amet, consectetur adipiscing elit, sed do eiusmod tempor</p>
</div>
<div class="card" style="left:677px;top:1028px">
  <div class="icon-dot maroon" style="left:16px;top:12px"><svg width="40" height="40" viewBox="0 0 40 40" fill="none" stroke="#fff" stroke-width="1.6"><ellipse cx="20" cy="20" rx="15" ry="6"/><ellipse cx="20" cy="20" rx="15" ry="6" transform="rotate(60 20 20)"/><ellipse cx="20" cy="20" rx="15" ry="6" transform="rotate(-60 20 20)"/></svg></div>
  <h3 style="left:120px;top:22px">Problem Heading</h3>
  <p style="left:120px;top:48px">Lorem ipsum dolor sit amet, consectetur adipiscing elit, sed do eiusmod tempor</p>
</div>
<div class="card" style="left:677px;top:1181px">
  <div class="icon-dot maroon" style="left:16px;top:12px"><svg width="40" height="40" viewBox="0 0 40 40" fill="none" stroke="#fff" stroke-width="1.6"><circle cx="20" cy="16" r="9"/><path d="M14 25 V34 H26 V25"/></svg></div>
  <h3 style="left:122px;top:22px">Problem Heading</h3>
  <p style="left:122px;top:48px">Lorem ipsum dolor sit amet, consectetur adipiscing elit, sed do eiusmod tempor</p>
</div>

<!-- Solutions -->
<h2 class="title" style="top:1420px">Solutions</h2>
<div class="title-rule" style="top:1479px;left:574px"></div>
<div class="link green" style="left:460px;top:1551px;width:115px"></div>
<div class="link green" style="left:460px;top:1706px;width:185px"></div>
<div class="link green" style="left:460px;top:1856px;width:115px"></div>
<div class="link green v" style="left:573px;top:1551px;height:309px"></div>

<div class="card" style="left:73px;top:1498px">
  <h3 style="left:50px;top:22px">Solution Heading</h3>
  <p style="left:50px;top:48px;width:236px">Lorem ipsum dolor sit amet, consectetur adipiscing elit sed do eiusm</p>
  <div class="icon-dot green" style="left:292px;top:12px"><svg width="40" height="40" viewBox="0 0 40 40" fill="none" stroke="#fff" stroke-width="1.6"><circle cx="20" cy="20" r="8"/><path d="M20 6 V11 M20 29 V34 M6 20 H11 M29 20 H34"/></svg></div>
</div>
<div class="card" style="left:73px;top:1648px">
  <h3 style="left:52px;top:22px">Solution Heading</h3>
  <p style="left:52px;top:48px;width:236px">Lorem ipsum dolor sit amet, consectetur adipiscing elit sed do eiusm</p>
  <div class="icon-dot green" style="left:292px;top:12px"><svg width="40" height="40" viewBox="0 0 40 40" fill="none" stroke="#fff" stroke-width="1.6"><rect x="8" y="10" width="24" height="16"/><path d="M4 30 H36"/></svg></div>
</div>
<div class="card" style="left:73px;top:1801px">
  <h3 style="left:54px;top:22px">Solution Heading</h3>
  <p style="left:54px;top:48px;width:236px">Lorem ipsum dolor sit amet, consectetur adipiscing elit sed do eiusm</p>
  <div class="icon-dot green" style="left:292px;top:12px"><svg width="40" height="40" viewBox="0 0 40 40" fill="none" stroke="#fff" stroke-width="1.6"><path d="M8 32 V24 M15 32 V18 M22 32 V20 M29 32 V12 M6 22 L16 12 L24 16 L34 6"/></svg></div>
</div>
<div class="ring" style="left:642px;top:1484px;width:452px;height:452px">
  <div class="fill" role="img" aria-label="Smiling businesswoman holding an open laptop" style="background:linear-gradient(170deg,#f1f1f3,#dcdde3 50%,#6c7bc0 80%,#2a2a35)"></div>
</div>

<!-- Benefits -->
<div class="benefits-bg"></div>
<div class="divider" style="top:2041px"></div>
<h2 class="title" style="top:2092px"><span class="light">Our </span>Benefits</h2>
<div class="title-rule" style="top:2153px"></div>

<div class="diamond" style="left:114px;top:2241px"></div>
<div class="diamond hot" style="left:471px;top:2241px"></div>
<div class="diamond" style="left:828px;top:2241px"></div>
<div class="diamond" style="left:292px;top:2439px"></div>
<div class="diamond" style="left:650px;top:2439px"></div>

<div class="d-copy" style="left:127px;top:2262px">
  <svg width="60" height="60" viewBox="0 0 60 60" fill="none" stroke="#163a77" stroke-width="2"><circle cx="30" cy="32" r="12"/><circle cx="30" cy="32" r="5"/><path d="M30 8 V14 M14 16 L18 20 M46 16 L42 20 M10 32 H16 M44 32 H50"/></svg>
  <h4>Benefit Heading</h4>
  <p>Lorem ipsum dolor sit amet, consectetur adipiscing elit, sed do eiusmod tempor incidi</p>
</div>
<div class="d-copy hot" style="left:484px;top:2262px">
  <svg width="60" height="60" viewBox="0 0 60 60" fill="none" stroke="#fff" stroke-width="2"><circle cx="30" cy="18" r="8"/><path d="M14 50 V40 C14 34 22 32 30 32 C38 32 46 34 46 40 V50"/></svg>
  <h4>Team Consulting</h4>
  <p>Lorem ipsum dolor sit amet, consectetur adipiscing elit, sed do eiusmod tempor incidi</p>
  <svg width="20" height="24" viewBox="0 0 20 24" style="margin-top:12px" fill="none" stroke="#fff" stroke-width="1.5"><path d="M10 2 V20 M4 14 L10 20 L16 14"/></svg>
</div>
<div class="d-copy" style="left:841px;top:2262px">
  <svg width="60" height="60" viewBox="0 0 60 60" fill="none" stroke="#163a77" stroke-width="2"><circle cx="30" cy="26" r="14"/><path d="M24 40 V50 H36 V40"/></svg>
  <h4>Benefit Heading</h4>
  <p>Lorem ipsum dolor sit amet, consectetur adipiscing elit, sed do eiusmod tempor incidi</p>
</div>
<div class="d-copy" style="left:305px;top:2460px">
  <svg width="60" height="60" viewBox="0 0 60 60" fill="none" stroke="#163a77" stroke-width="2"><rect x="8" y="8" width="44" height="44"/><path d="M8 16 H52"/><circle cx="30" cy="34" r="11"/><circle cx="30" cy="34" r="5"/></svg>
  <h4>Optimization</h4>
  <p>Lorem ipsum dolor sit amet, consectetur adipiscing elit, sed do eiusmod tempor incidi</p>
</div>
<div class="d-copy" style="left:663px;top:2460px">
  <svg width="60" height="60" viewBox="0 0 60 60" fill="none" stroke="#163a77" stroke-width="2"><circle cx="30" cy="30" r="20" stroke-dasharray="6 3"/><circle cx="30" cy="30" r="13"/><circle cx="30" cy="30" r="6"/></svg>
  <h4>Benefit Heading</h4>
  <p>Lorem ipsum dolor sit amet, consectetur adipiscing elit, sed do eiusmod tempor incidi</p>
</div>

<div class="quote">
  <div class="mark">“</div>
  <blockquote>We cannot solve our problems with the same thinking we used when we created them</blockquote>
  <cite>- Harold Whitcombe</cite>
</div>

<!-- Testimonials -->
<h2 class="title" style="top:3080px;font-size:34px"><span class="light">What Our Client </span>are Saying</h2>
<div class="t-card" style="left:-220px;opacity:.6"></div>
<div class="t-card" style="left:151px"><div class="q">66</div><p>"Lorem ipsum dolor sit amet, consectetur adipiscing elit, sed do eiusmod tempor incididunt ut labore et dolore magna aliqua. Ut enim ad minim veniam, quis nostrud exercitation ullamco laboris nisi ut aliquip ex ea commodo consequatoute</p><div class="who"><div class="avatar"></div><div><div class="stars">★★★★★</div><b>Mara Ellison</b></div></div></div>
<div class="t-card" style="left:453px"><div class="q">66</div><p>"Lorem ipsum dolor sit amet, consectetur adipiscing elit, sed do eiusmod tempor incididunt ut labore et dolore magna aliqua. Ut enim ad minim veniam, quis nostrud exercitation ullamco laboris nisi ut aliquip ex ea commodo consequatoute</p><div class="who"><div class="avatar"></div><div><div class="stars">★★★★★</div><b>Mara Ellison</b></div></div></div>
<div class="t-card" style="left:761px"><div class="q">66</div><p>"Lorem ipsum dolor sit amet, consectetur adipiscing elit, sed do eiusmod tempor incididunt ut labore et dolore magna aliqua. Ut enim ad minim veniam, quis nostrud exercitation ullamco laboris nisi ut aliquip ex ea commodo consequatoute</p><div class="who"><div class="avatar"></div><div><div class="stars">★★★★★</div><b>Mara Ellison</b></div></div></div>
<div class="t-card" style="left:1125px;opacity:.6"></div>
<div class="arrow" style="left:94px">❮</div>
<div class="arrow" style="left:1090px">❯</div>

<!-- Contact -->
<div class="footer-bg"></div>
<section class="contact">
  <h2>Get <b>in Touch with Us</b></h2>
  <div class="field" style="left:155px;top:131px;width:296px;height:41px"><i></i>First Name*</div>
  <div class="field" style="left:465px;top:131px;width:294px;height:41px"><i></i>Last Name*</div>
  <div class="field" style="left:155px;top:186px;width:296px;height:40px"><i></i>Email address*</div>
  <div class="field" style="left:465px;top:186px;width:294px;height:40px"><i></i>Phone*</div>
  <div class="field" style="left:155px;top:240px;width:604px;height:94px;align-items:flex-start;padding-top:14px"><i></i>Leave Message</div>
  <div class="submit">Submit Now ›</div>
</section>

<!-- Footer -->
<div class="f-logo">Brightpath</div>
<p class="f-about">Lorem ipsum dolor sit amet, consectetur adipiscing elit, sed do eiusmod tempor incididunt ut labore et dolore magna aliqua. Quis ipsum suspendisse ultrices gravida</p>
<div class="f-head" style="left:414px">NAVGATION</div>
<ul class="f-list" style="left:428px"><li>Home</li><li>About us</li><li>Services</li><li>Contact us</li></ul>
<div class="f-head" style="left:630px">CONTACT US</div>
<div class="f-item" style="top:4100px"><div class="dot"><svg width="16" height="12" viewBox="0 0 16 12" fill="none" stroke="#6b7c98" stroke-width="1.5"><rect x="1" y="1" width="14" height="10"/><path d="M1 1 L8 7 L15 1"/></svg></div><span>Email us at<br>info@brightpath.example</span></div>
<div class="f-item" style="top:4168px"><div class="dot"><svg width="14" height="14" viewBox="0 0 14 14" fill="#6b7c98"><path d="M3 1 L5 4 L4 6 C5 8 6 9 8 10 L10 9 L13 11 L11 13 C6 13 1 8 1 3 Z"/></svg></div><span>Phone Support<br>(555) 014 2286</span></div>
<div class="f-head" style="left:899px">FOLLOW US</div>
<div class="social" style="left:901px"></div>
<div class="social" style="left:956px"></div>
<div class="social" style="left:1010px"></div>
<div class="footer-bar">© 2025 Company Name | All Rights Reserved</div>

</body>
</html>
```